Property Developer Business card design

we need a business card design + printing for a new Property developer company based in melbourne.
We are a group of investors investing in a property developer business. We have more projects involved in residential property as opposed to commercial property but we are involved in both market. we also provide consulting services with overseas investors willing to invest in the australian property market.
Updates
I have uploaded the logo. I'm not very convince with the colors of my logo... any suggestion please?.
Thanks guys!
Target Market(s)
property investors or person willing to purchase investment property
Industry/Entity Type
Residential
Contact Information for Business Card
Harbourne Capital Australia Pty Ltd
Look and feel
Each slider illustrates characteristics of the customer's brand and the style your logo design should communicate.

```html
<!DOCTYPE html>
<html lang="en">
<head>
<meta charset="utf-8">
<title>Harbourne Capital Australia — Business Cards</title>
<link rel="stylesheet" href="https://fonts.googleapis.com/css2?family=Exo+2:wght@600&family=Questrial&family=Tinos&display=swap">
<style>
  :root {
    --bg: #dcdcdc;
    --brand-blue: #0a7bc1;
    --sky-blue: #1a86cf;
    --brand-red: #be2126;
    --ink: #111111;
    --paper: #ffffff;
  }
  * { margin: 0; padding: 0; box-sizing: border-box; }
  html, body { width: 1200px; height: 985px; overflow: hidden; }
  body {
    background: var(--bg);
    position: relative;
    font-family: "Questrial", sans-serif;
  }
  .card {
    position: absolute;
    width: 640px;
    height: 366px;
    border-radius: 26px;
    overflow: hidden;
    box-shadow: 0 6px 18px rgba(0,0,0,0.18);
  }
  /* Back side */
  .card--back {
    left: 430px; top: 50px;
    background: var(--brand-blue);
    color: var(--paper);
  }
  .card--back .wordmark {
    position: absolute;
    left: 0; right: 0; top: 120px;
    text-align: center;
    font-family: "Exo 2", sans-serif;
    font-weight: 600;
    font-size: 40px;
    color: var(--paper);
  }
  .card--back .legal-name {
    position: absolute;
    left: 0; right: 0; top: 228px;
    text-align: center;
    font-family: "Tinos", serif;
    font-size: 27px;
    letter-spacing: 0.5px;
  }
  /* Front side */
  .card--front {
    left: 130px; top: 470px;
    background: var(--paper);
  }
  .card--front .wave {
    position: absolute; left: 0; bottom: 0;
    width: 640px; height: 366px;
  }
  .card--front .wordmark {
    position: absolute;
    left: 40px; top: 34px;
    font-family: "Exo 2", sans-serif;
    font-weight: 600;
    font-size: 30px;
    color: var(--sky-blue);
  }
  .person {
    position: absolute;
    left: 40px; top: 118px;
    font-variant: small-caps;
  }
  .person .name { color: var(--sky-blue); font-size: 24px; }
  .person .role { color: var(--ink); font-size: 15px; letter-spacing: 0.5px; margin-top: 2px; }
  .contact {
    position: absolute;
    left: 340px; top: 104px;
    font-size: 17px;
    line-height: 1.3;
    color: var(--ink);
  }
  .contact .address { font-variant: small-caps; font-size: 19px; margin-bottom: 10px; }
  .contact .label { color: var(--brand-red); font-variant: small-caps; }
  .contact .email { color: var(--sky-blue); font-family: "Tinos", serif; font-size: 16px; margin-top: 2px; }
</style>
</head>
<body>
  <section class="card card--back" aria-label="Card back">
    <div class="wordmark">Harbourne Capital Australia</div>
    <div class="legal-name">Harbourne Capital Australia Pty Ltd</div>
  </section>

  <section class="card card--front" aria-label="Card front">
    <svg class="wave" viewBox="0 0 640 366" aria-hidden="true">
      <path d="M0 196 C 150 250, 300 330, 640 292 L640 366 L0 366 Z" fill="var(--sky-blue)"/>
      <path d="M0 206 C 150 264, 300 346, 640 310 L640 366 L0 366 Z" fill="var(--brand-red)"/>
    </svg>
    <div class="wordmark">Harbourne Capital Australia</div>
    <div class="person">
      <div class="name">Daniel Reyes</div>
      <div class="role">Managing Director</div>
    </div>
    <div class="contact">
      <div class="address">17 Saltbush Drive<br>Westmeadow VIC 3049</div>
      <div><span class="label">Telephone :</span> +61 3 9000 4821</div>
      <div><span class="label">Mobile :</span> 0400 182 556</div>
      <div class="email">daniel.reyes@harbournecapital.com.au</div>
    </div>
  </section>
</body>
</html>
```